Business Card Project

We are a small consulting firm. You can experiment with any design.
Must have:
1) Company name - TOLVIN International
2) Company slogan - simple solutions for complex problems
3) Name/Title/Phone/Email/WWW/ - use anything you like as an example.

Industry/Entity Type

Business

```html
<!DOCTYPE html>
<html lang="en">
<head>
<meta charset="utf-8">
<title>TOLVIN International – Business Card</title>
<link rel="stylesheet" href="https://fonts.googleapis.com/css2?family=Fira+Sans:ital,wght@0,400;0,500;1,400;1,500&display=swap">
<style>
  :root {
    --page-bg: #e6eaef;
    --card-bg: #eef3f3;
    --card-bg-edge: #e3eaea;
    --ink: #3f4648;
    --accent: #1e8fe6;
    --name-blue: #1f80d6;
    --brand-dark: #414a4d;
  }
  * { margin: 0; padding: 0; box-sizing: border-box; }
  html, body {
    width: 1200px;
    height: 1000px;
    overflow: hidden;
    background: var(--page-bg);
    font-family: "Fira Sans", Arial, sans-serif;
  }
  .canvas { position: relative; width: 1200px; height: 1000px; }
  .card {
    position: absolute;
    width: 697px;
    height: 421px;
    overflow: hidden;
    background: linear-gradient(100deg, var(--card-bg) 0%, var(--card-bg) 55%, var(--card-bg-edge) 100%);
  }
  .card--front { left: 52px; top: 53px; }
  .card--back { left: 444px; top: 520px; width: 695px; height: 418px; }

  .slogan {
    position: absolute;
    left: 34px;
    top: 186px;
    font-style: italic;
    font-weight: 500;
    font-size: 35px;
    letter-spacing: 0.2px;
    color: var(--ink);
    white-space: nowrap;
  }
  .slogan .highlight { color: var(--accent); }

  .brand {
    position: absolute;
    left: 24px;
    top: 70px;
    display: flex;
    align-items: center;
    gap: 24px;
  }
  .brand__dot { width: 104px; height: 104px; flex: none; }
  .brand__name {
    font-weight: 400;
    font-size: 50px;
    letter-spacing: 1px;
    color: var(--brand-dark);
    white-space: nowrap;
  }

  .person {
    position: absolute;
    left: 48px;
    top: 255px;
    width: 176px;
    text-align: center;
    font-style: italic;
    font-weight: 500;
    color: var(--name-blue);
  }
  .person__name { font-size: 31px; line-height: 40px; white-space: nowrap; }
  .person__title { font-size: 27px; line-height: 44px; }

  .contact {
    position: absolute;
    left: 346px;
    top: 252px;
    list-style: none;
    font-style: italic;
    font-weight: 500;
    font-size: 18px;
    line-height: 26px;
    color: var(--ink);
    letter-spacing: 1.5px;
    white-space: nowrap;
  }
  .contact__label { display: inline-block; width: 20px; }
  .contact__value--wide { letter-spacing: 5px; }
  .contact__value--spaced { letter-spacing: 3px; }
</style>
</head>
<body>
<main class="canvas">
  <section class="card card--front" aria-label="Business card front">
    <p class="slogan">simple <span class="highlight">solutions</span> for complex problems</p>
  </section>

  <section class="card card--back" aria-label="Business card back">
    <div class="brand">
      <svg class="brand__dot" viewBox="0 0 104 104" aria-hidden="true">
        <circle cx="52" cy="52" r="48" fill="var(--accent)"/>
      </svg>
      <span class="brand__name">TOLVIN International</span>
    </div>

    <div class="person">
      <p class="person__name">Your Name</p>
      <p class="person__title">Tittle</p>
    </div>

    <ul class="contact">
      <li><span class="contact__label">W</span> <span class="contact__value--spaced">www.tolvin.com</span></li>
      <li><span class="contact__label">E</span>info@tolvinsolutions.com</li>
      <li><span class="contact__label">P</span> <span class="contact__value--wide">123-456-7890</span></li>
      <li><span class="contact__label">F</span> <span class="contact__value--wide">123-456-7890</span></li>
    </ul>
  </section>
</main>
</body>
</html>
```